Zolvix Activewear business card design

I need a business card designed for my activewear business. I would like to use the colours pink, purple white and blue. please see attached logo. please include (name) Harriet Lomberg (phone) 0417862035 (email) hattiezolvix@mailbox.example (ABN) 48193570264 . please include - Free shipping on all orders over $100

Target Market(s)

female

Contact Information for Business Card

Colors

Designer to choose colors to be used in the design.

Requirements
Must have
• I need a business card designed for my activewear business. I would like to use the colours pink, purple white and blue. please see attached logo. please include (name) Harriet Lomberg (phone) 0417862035 (email) hattiezolvix@mailbox.example (ABN) 48193570264 . please include - Free shipping on all orders over $100

```html
<!DOCTYPE html>
<html lang="en">
<head>
<meta charset="utf-8">
<title>Zolvix Activewear – Business Card</title>
<link rel="stylesheet" href="https://fonts.googleapis.com/css2?family=Ubuntu:wght@500;700&family=Open+Sans:wght@400;600&display=swap">
<style>
  :root {
    --backdrop: #2a2a2c;
    --card-navy: #1c3564;
    --card-navy-deep: #182d57;
    --edge-purple: #a03ea6;
    --brand-pink: #e07cb3;
    --accent-magenta: #c0358f;
    --text-white: #f4f4f8;
  }
  * { box-sizing: border-box; margin: 0; padding: 0; }
  html, body {
    width: 1200px; height: 895px; overflow: hidden;
    background: var(--backdrop);
  }
  .stage {
    width: 1200px; height: 895px;
    display: flex; justify-content: center; align-items: center; gap: 130px;
  }
  .card {
    position: relative;
    width: 400px; height: 700px;
    border-radius: 26px;
    background: var(--card-navy);
    border: 6px solid var(--edge-purple);
    overflow: hidden;
    font-family: "Open Sans", sans-serif;
    color: var(--text-white);
  }

  /* back side */
  .card-back .pattern-field {
    position: absolute; inset: 0;
    background: linear-gradient(160deg, #22406f 0%, var(--card-navy) 55%, var(--card-navy-deep) 100%);
  }
  .card-back .center-mark {
    position: absolute; left: 50%; top: 45%;
    transform: translate(-50%, -50%);
    width: 44px; height: 44px; border-radius: 50%;
    border: 3px solid var(--brand-pink);
  }
  .card-back .brand-name {
    position: absolute; left: 0; right: 0; bottom: 96px;
    text-align: center;
    font-family: "Ubuntu", sans-serif; font-weight: 700;
    font-size: 34px; letter-spacing: 1px;
    color: var(--edge-purple);
  }
  .card-back .shipping-offer {
    position: absolute; left: 0; right: 0; bottom: 52px;
    text-align: center;
    font-size: 15px; letter-spacing: 0.4px;
    color: var(--text-white);
  }

  /* front side */
  .card-front .brand-lockup {
    position: absolute; top: 52px; right: 40px;
    display: flex; align-items: center; gap: 12px;
  }
  .card-front .brand-dot {
    width: 30px; height: 30px; border-radius: 50%;
    border: 3px solid var(--brand-pink);
  }
  .card-front .brand-name {
    font-family: "Ubuntu", sans-serif; font-weight: 700;
    font-size: 26px; color: var(--brand-pink);
  }
  .brand-rule {
    position: absolute; top: 104px; right: 40px;
    width: 200px; height: 3px;
    background: linear-gradient(90deg, transparent, var(--accent-magenta));
  }
  .contact-block {
    position: absolute; top: 200px; left: 0; right: 0;
    text-align: center;
  }
  .person-name {
    font-family: "Ubuntu", sans-serif; font-weight: 500;
    font-size: 34px; color: var(--brand-pink);
    letter-spacing: 0.5px;
  }
  .contact-icons {
    display: flex; justify-content: center; gap: 20px;
    margin-top: 34px;
  }
  .contact-icons svg { width: 38px; height: 38px; }
  .contact-line {
    font-size: 19px; line-height: 1.5; letter-spacing: 0.3px;
  }
  .contact-line.phone { margin-top: 22px; }
  .divider {
    width: 70px; height: 3px; background: var(--brand-pink);
    margin: 40px auto 34px;
  }
  .abn { font-size: 20px; letter-spacing: 0.5px; }
</style>
</head>
<body>
<main class="stage">

  <section class="card card-back" aria-label="Card back">
    <div class="pattern-field" role="img" aria-label="Faint repeating heart outline pattern on navy"></div>
    <div class="center-mark"></div>
    <div class="brand-name">Zolvix Activewear</div>
    <p class="shipping-offer">Free shipping on all orders over $100</p>
  </section>

  <section class="card card-front" aria-label="Card front">
    <div class="brand-lockup">
      <span class="brand-dot"></span>
      <span class="brand-name">Zolvix Activewear</span>
    </div>
    <div class="brand-rule"></div>

    <div class="contact-block">
      <h1 class="person-name">Harriet Lomberg</h1>

      <div class="contact-icons">
        <svg viewBox="0 0 38 38" aria-label="Phone">
          <circle cx="19" cy="19" r="16.5" fill="none" stroke="#a03ea6" stroke-width="3"/>
          <rect x="13" y="11" width="12" height="16" rx="2" fill="none" stroke="#e07cb3" stroke-width="2"/>
          <line x1="17" y1="24" x2="21" y2="24" stroke="#e07cb3" stroke-width="1.6"/>
        </svg>
        <svg viewBox="0 0 38 38" aria-label="Email">
          <circle cx="19" cy="19" r="16.5" fill="none" stroke="#a03ea6" stroke-width="3"/>
          <rect x="11" y="13" width="16" height="12" rx="1.5" fill="#e07cb3"/>
          <polyline points="11,13.5 19,20 27,13.5" fill="none" stroke="#1c3564" stroke-width="1.6"/>
        </svg>
      </div>

      <p class="contact-line phone">0417862035</p>
      <p class="contact-line email">hattiezolvix@mailbox.example</p>

      <div class="divider"></div>

      <p class="abn">(ABN) 48193570264</p>
    </div>
  </section>

</main>
</body>
</html>
```